Author/ Speaker Business Card design

I need a business card designed that will go with the branding that is already on my book and website. I like clean and straightforward, but I am not opposed to something more 'innovative'.

Target Market(s)

Colleges and Universities, educational institutions

Industry/Entity Type

Education

Contact Information for Business Card

Standard size. It should be able to be printed on good quality white or ivory paper.

Font styles to use
Sans Serif

Colors
0355a3

Requirements
Must have
• There's a blue on my website. It should have some blue. My logo is at the top. It should have the logo incorporated somewhere on it. My name, Author | Speaker | Teacher | Trainer, my phone number (+31 64-207 5819), my email address (milo@theboldlearner.example), Social media icons (posts, Photos, LinkedIn) with the addresses (posts @writermilofenwick, Photos - theboldlearner, LinkedIn - theboldlearner) By they way, the website is www.theboldlearner.example. There is a photo of the book on the website. Also, my full name is Milo Fenwick
Nice to have
• Try to use the font that is on the website and book. Also, if you could get that blue, that would be great.
Should not have
• My photo

```html
<!DOCTYPE html>
<html lang="en">
<head>
<meta charset="utf-8">
<title>Milo Fenwick – Business Card</title>
<link href="https://fonts.googleapis.com/css2?family=Source+Sans+3:wght@300;400;600;700&display=swap" rel="stylesheet">
<style>
  :root {
    --ink-blue: #0a5fae;
    --band-blue: #0069b4;
    --band-edge: #1d44a0;
    --card-line: #e2e2e2;
    --paper: #ffffff;
  }
  * { margin: 0; padding: 0; box-sizing: border-box; }
  html, body {
    width: 751px;
    height: 1200px;
    overflow: hidden;
    background: var(--paper);
    font-family: "Source Sans 3", sans-serif;
    color: var(--ink-blue);
  }
  .card {
    position: absolute;
    left: 81px;
    top: 128px;
    width: 592px;
    height: 946px;
    border: 2px solid var(--card-line);
    background: var(--paper);
  }
  .brand {
    position: absolute;
    top: 98px;
    left: 0;
    width: 100%;
    display: flex;
    justify-content: center;
    align-items: center;
    gap: 14px;
  }
  .brand-mark {
    width: 34px;
    height: 34px;
    background: var(--ink-blue);
  }
  .brand-name {
    font-size: 40px;
    font-weight: 700;
    color: var(--ink-blue);
    letter-spacing: -0.5px;
  }
  .person {
    position: absolute;
    top: 328px;
    left: 0;
    width: 100%;
    text-align: center;
  }
  .person-name {
    font-size: 47px;
    font-weight: 700;
    letter-spacing: -0.3px;
    line-height: 1;
  }
  .person-roles {
    margin-top: 18px;
    font-size: 37px;
    font-weight: 300;
    line-height: 1;
  }
  .contacts {
    position: absolute;
    top: 582px;
    left: 41px;
    list-style: none;
    font-size: 29px;
    font-weight: 400;
  }
  .contact-row {
    display: flex;
    align-items: center;
    height: 51px;
  }
  .contact-label {
    width: 104px;
    flex: none;
  }
  .contact-icon {
    width: 104px;
    flex: none;
    display: flex;
    padding-left: 24px;
  }
  .contact-icon span {
    display: block;
    width: 30px;
    height: 30px;
    background: var(--ink-blue);
    border-radius: 4px;
  }
  .web-band {
    position: absolute;
    left: -2px;
    right: -2px;
    bottom: -2px;
    height: 81px;
    background: var(--band-blue);
    border-top: 5px solid var(--band-edge);
    color: var(--paper);
    font-size: 32px;
    font-weight: 400;
    display: flex;
    align-items: center;
    justify-content: center;
  }
</style>
</head>
<body>
  <div class="card">
    <div class="brand">
      <span class="brand-mark"></span>
      <span class="brand-name">The Bold Learner</span>
    </div>

    <div class="person">
      <h1 class="person-name">MILO FENWICK</h1>
      <p class="person-roles">Author | Speaker | Teacher | Trainer</p>
    </div>

    <ul class="contacts">
      <li class="contact-row"><span class="contact-label">Phone:</span><span>+31 64-207 5819</span></li>
      <li class="contact-row"><span class="contact-label">Email:</span><span>milo@theboldlearner.example</span></li>
      <li class="contact-row"><span class="contact-icon"><span></span></span><span>posts @writermilofenwick</span></li>
      <li class="contact-row"><span class="contact-icon"><span></span></span><span>&nbsp;Photos - theboldlearner,</span></li>
      <li class="contact-row"><span class="contact-icon"><span></span></span><span>theboldlearner)</span></li>
    </ul>

    <div class="web-band">www.theboldlearner.example</div>
  </div>
</body>
</html>
```